I'm doing a recreational cannabis grow business here in the Columbia Gorge scenic area . I'm looking for a business card similar to the Tollervey Lodge logo,except for the sun raise to be pot leafs.
The Gorge mountains,the river with the sun coming off the water between the mountains with the pot leaf rays.
All print would be on the back side
Kick ass simple black and gold or kick ass colorful

Target Market(s)

Retailers

Industry/Entity Type

Business

Contact Information for Business Card

Brindlecroft Acres
Grown with care in the Marrowind Valley
Email brindlecroftacresllc@mailvane.net

Font styles to use
Other font styles liked:
• What the artist thinks

Colors

Designer to choose colors to be used in the design.

Requirements
Must have
• Nice to look at . Like that bottle of wine you buy because the label graphics told you too.
Nice to have
• It's in my description
• You can lookup the Tollervey Logde in Stevenson Wa and check out there logo, and I'm always up for ideas.
• Color and fonts should be what the artist thinks best
Should not have
• Boring

```html
<!DOCTYPE html>
<html lang="en">
<head>
<meta charset="utf-8">
<title>Brindlecroft Acres Business Card</title>
<link rel="stylesheet" href="https://fonts.googleapis.com/css2?family=Open+Sans:wght@400;600;700&display=swap">
<style>
  :root {
    --backdrop: #e9e9e9;
    --card: #ffffff;
    --gold: #f0a043;
    --forest: #1f7a45;
    --river: #2b7ac4;
    --sun: #f29a2e;
  }
  * { margin: 0; padding: 0; box-sizing: border-box; }
  html, body {
    width: 1200px;
    height: 800px;
    overflow: hidden;
    background: var(--backdrop);
    font-family: "Open Sans", Arial, sans-serif;
  }
  .canvas {
    position: relative;
    width: 1200px;
    height: 800px;
  }
  .card {
    position: absolute;
    width: 560px;
    height: 320px;
    background: var(--card);
    box-shadow: 0 4px 14px rgba(0,0,0,0.12);
    overflow: hidden;
  }
  .card-front { left: 320px; top: 50px; }
  .card-back { left: 320px; top: 420px; }

  /* front */
  .front-frame {
    position: absolute;
    inset: 20px;
    border: 2px solid var(--gold);
  }
  .front-brand {
    position: absolute;
    left: 0; right: 0; top: 62px;
    text-align: center;
  }
  .brand-dot {
    display: block;
    margin: 0 auto 14px;
    width: 70px;
    height: 70px;
    border-radius: 50%;
    background: var(--sun);
  }
  .brand-name {
    color: var(--forest);
    font-weight: 700;
    font-size: 32px;
    line-height: 1.1;
    white-space: nowrap;
  }
  .brand-tagline {
    color: var(--river);
    font-weight: 600;
    font-size: 12px;
    margin-top: 4px;
    white-space: nowrap;
  }
  .email-band {
    position: absolute;
    left: 250px;
    right: 20px;
    top: 250px;
    height: 34px;
    background: var(--gold);
    color: #fff;
    font-size: 15px;
    line-height: 34px;
    padding-left: 14px;
    white-space: nowrap;
  }

  /* back */
  .back-brand {
    position: absolute;
    left: 0;
    width: 250px;
    top: 84px;
    text-align: center;
  }
  .back-brand .brand-dot {
    width: 56px;
    height: 56px;
    margin-bottom: 14px;
  }
  .back-brand .brand-name { font-size: 19px; }
  .back-brand .brand-tagline { font-size: 8px; margin-top: 2px; }
  .divider {
    position: absolute;
    left: 250px;
    top: 34px;
    width: 2px;
    height: 252px;
    background: linear-gradient(to bottom, transparent, var(--gold) 15%, var(--gold) 85%, transparent);
  }
  .contact {
    position: absolute;
    left: 290px;
    top: 52px;
    color: var(--river);
  }
  .contact-name { font-size: 19px; font-weight: 700; }
  .contact-position { font-size: 15px; margin-top: 4px; }
  .contact-list { list-style: none; margin-top: 34px; }
  .contact-list li {
    display: flex;
    align-items: center;
    gap: 8px;
    font-size: 15px;
    margin-bottom: 12px;
  }
  .contact-icon { width: 14px; height: 14px; flex: none; }
</style>
</head>
<body>
<main class="canvas">

  <section class="card card-front" aria-label="Business card front">
    <div class="front-frame"></div>
    <div class="front-brand">
      <span class="brand-dot"></span>
      <div class="brand-name">Brindlecroft Acres</div>
      <div class="brand-tagline">Grown with care in the Marrowind Valley</div>
    </div>
    <div class="email-band">brindlecroftacresllc@mailvane.net</div>
  </section>

  <section class="card card-back" aria-label="Business card back">
    <div class="back-brand">
      <span class="brand-dot"></span>
      <div class="brand-name">Brindlecroft Acres</div>
      <div class="brand-tagline">Grown with care in the Marrowind Valley</div>
    </div>
    <div class="divider"></div>
    <div class="contact">
      <div class="contact-name">Your Name</div>
      <div class="contact-position">Position</div>
      <ul class="contact-list">
        <li>
          <svg class="contact-icon" viewBox="0 0 14 14" aria-hidden="true">
            <rect x="3.5" y="1" width="7" height="12" rx="1.2" fill="none" stroke="#f0a043" stroke-width="1.4"/>
            <circle cx="7" cy="10.8" r="0.8" fill="#f0a043"/>
          </svg>
          <span>000.000.0000</span>
        </li>
        <li>
          <svg class="contact-icon" viewBox="0 0 14 14" aria-hidden="true">
            <rect x="1" y="3" width="12" height="8.5" fill="#f0a043"/>
            <path d="M1 3 L7 8 L13 3" fill="none" stroke="#fff" stroke-width="1.2"/>
          </svg>
          <span>name@email.com</span>
        </li>
      </ul>
    </div>
  </section>

</main>
</body>
</html>
```